Business Card Design for Varnok Facility Services

We are looking for a Business Card Design for the Company "Varnok Facility Services."
Front side:
- Company Logo (small)
- Company Name, address, pohone, website and personal data.
- white background, for text e.g. company colors (blue or green like in the logo)
Please use following data:
Company data:
Varnok Facility Services Tulbrecht
Kirchmattweg 12
6331 Cham
www.varnok-fs.ch
Person data:
Ruben Tulbrecht
Geschäftsführer
+41 76 519 84 60
info@varnok-fs.ch
Back side:
could be colored in blue or green
please use a big logo sing and some smaller icons to say what is all beeing offered in facility services, like cleaning, maintenance cleaning
industrial cleaning, caretaking, gardening, disposal. There is no need for everyone of the icons if there are similar or an icon is standing for more of them.
Cleaning Service
colors to use:
blue: HEX 246BB0
green: HEX 52B33E

```html
<!DOCTYPE html>
<html lang="de">
<head>
<meta charset="utf-8">
<title>Varnok Facility Services – Business Card</title>
<link rel="stylesheet" href="https://fonts.googleapis.com/css2?family=Arimo:wght@400;700&display=swap">
<style>
  :root {
    --brand-blue: #246BB0;
    --brand-green: #52B33E;
    --paper: #FFFFFF;
    --backdrop: #D6D6D6;
    --text-font: "Arimo", Arial, sans-serif;
  }
  * { box-sizing: border-box; margin: 0; padding: 0; }
  html, body { width: 1200px; height: 900px; overflow: hidden; }
  body { background: var(--backdrop); font-family: var(--text-font); position: relative; }

  .card {
    position: absolute;
    width: 560px;
    height: 362px;
    overflow: hidden;
    box-shadow: 0 6px 18px rgba(0,0,0,0.18);
  }
  .card-shape { position: absolute; inset: 0; width: 100%; height: 100%; }

  /* Back side */
  .card-back { left: 50px; top: 80px; background: var(--brand-blue); }
  .card-back .brand {
    position: absolute; left: 60px; top: 58px;
    display: flex; align-items: center; gap: 14px;
  }
  .brand-dot { width: 22px; height: 22px; border-radius: 50%; background: var(--brand-green); flex: none; }
  .card-back .brand-name {
    color: var(--paper); font-weight: 700; font-size: 31px; letter-spacing: 0.5px; line-height: 1.1;
  }
  .service-list {
    position: absolute; left: 40px; top: 150px;
    display: flex; gap: 14px; list-style: none;
  }
  .service { width: 78px; text-align: center; color: var(--paper); font-size: 12px; line-height: 1.2; }
  .service-icon {
    display: block; width: 40px; height: 40px; margin: 0 auto 8px;
    border-radius: 8px; background: rgba(82,179,62,0.55);
  }

  /* Front side */
  .card-front { left: 590px; top: 480px; background: var(--paper); }
  .card-front .brand {
    position: absolute; left: 70px; top: 64px;
    display: flex; align-items: center; gap: 12px;
  }
  .card-front .brand-name {
    color: var(--brand-blue); font-weight: 700; font-size: 27px; letter-spacing: 0.4px; line-height: 1.1;
  }
  .person { position: absolute; left: 70px; top: 165px; width: 170px; text-align: right; }
  .person-name { color: var(--brand-green); font-weight: 700; font-size: 19px; }
  .person-role { color: var(--brand-blue); font-size: 13px; margin-top: 4px; }
  .divider { position: absolute; left: 256px; top: 150px; width: 1.5px; height: 72px; background: var(--brand-green); }
  .contact-list { position: absolute; left: 272px; top: 154px; list-style: none; }
  .contact { display: flex; align-items: center; gap: 7px; color: var(--brand-blue); font-size: 13px; line-height: 22px; }
  .contact svg { width: 12px; height: 12px; flex: none; }
  .address {
    position: absolute; right: 24px; bottom: 20px;
    color: var(--paper); font-size: 14px;
  }
</style>
</head>
<body>

<section class="card card-back" aria-label="Business card back side">
  <svg class="card-shape" viewBox="0 0 560 362" preserveAspectRatio="none" aria-hidden="true">
    <path d="M0,362 L0,335 Q390,325 560,205 L560,362 Z" fill="var(--brand-green)"/>
    <path d="M70,356 Q410,330 560,228" fill="none" stroke="var(--brand-blue)" stroke-width="4"/>
  </svg>
  <div class="brand">
    <span class="brand-dot"></span>
    <span class="brand-name">Varnok Facility Services</span>
  </div>
  <ul class="service-list">
    <li class="service"><span class="service-icon" role="img" aria-label="Cleaning icon: bucket and squeegee"></span>Cleaning</li>
    <li class="service"><span class="service-icon" role="img" aria-label="Maintenance cleaning icon: office building"></span>Maintenance Cleaning</li>
    <li class="service"><span class="service-icon" role="img" aria-label="Industrial cleaning icon: factory"></span>Industrial Cleaning</li>
    <li class="service"><span class="service-icon" role="img" aria-label="Gardening icon: plant in hand"></span>Gardening</li>
    <li class="service"><span class="service-icon" role="img" aria-label="Disposal icon: recycling bag"></span>Disposal</li>
  </ul>
</section>

<section class="card card-front" aria-label="Business card front side">
  <svg class="card-shape" viewBox="0 0 560 362" preserveAspectRatio="none" aria-hidden="true">
    <path d="M150,362 Q430,320 560,120 L560,362 Z" fill="var(--brand-blue)"/>
    <path d="M175,342 Q430,300 545,100" fill="none" stroke="var(--brand-green)" stroke-width="6"/>
  </svg>
  <div class="brand">
    <span class="brand-dot"></span>
    <span class="brand-name">Varnok Facility Services</span>
  </div>
  <div class="person">
    <p class="person-name">Ruben Tulbrecht</p>
    <p class="person-role">Geschäftsführer</p>
  </div>
  <span class="divider" aria-hidden="true"></span>
  <ul class="contact-list">
    <li class="contact">
      <svg viewBox="0 0 12 12" aria-hidden="true"><path d="M2.5,1 L4.5,1 L5.2,3.5 L4,4.5 Q5,7 7.5,8 L8.5,6.8 L11,7.5 L11,9.5 Q10.5,11 9,11 Q1,10 1,3 Q1,1.5 2.5,1 Z" fill="var(--brand-green)"/></svg>
      +41 76 519 84 60
    </li>
    <li class="contact">
      <svg viewBox="0 0 12 12" aria-hidden="true"><rect x="0.8" y="2.3" width="10.4" height="7.4" fill="none" stroke="var(--brand-green)" stroke-width="1.3"/><path d="M1,2.6 L6,6.5 L11,2.6" fill="none" stroke="var(--brand-green)" stroke-width="1.3"/></svg>
      info@varnok-fs.ch
    </li>
    <li class="contact">
      <svg viewBox="0 0 12 12" aria-hidden="true"><circle cx="6" cy="6" r="5" fill="var(--brand-green)"/><path d="M1,6 H11 M6,1 Q3.5,6 6,11 M6,1 Q8.5,6 6,11" fill="none" stroke="var(--paper)" stroke-width="0.9"/></svg>
      www.varnok-fs.ch
    </li>
  </ul>
  <p class="address">Kirchmattweg 12, 6331 Cham</p>
</section>

</body>
</html>
```